New Summit Tile Billboard at HQ

Looking to design a catchy image / theme for a billboard located just above our corporate HQ showroom and warehouse, along the service road of a 6-lane highway. Billboard measures 8ft x 24 ft. Would like to highlight that the store location is directly beneath the sign.

We are a retail and wholesale business selling premium flooring, ready to assemble cabinets, and granite countertops. See image ideas attached. Our information:
NAME: Summit Tile, Cabinets, Countertops
ADDRESS: 417 W. Hwy 82, Maple Ridge, OK 75284
WEBSITE: www.summittilehub.example
PHONE: 555-8-TILEUP (972-845-3887)

```html
<!DOCTYPE html>
<html lang="en">
<head>
<meta charset="utf-8">
<title>Summit Tile Billboard</title>
<link rel="stylesheet" href="https://fonts.googleapis.com/css2?family=Montserrat:wght@400;700;800;900&display=swap">
<style>
  :root {
    --bg: #5f5f5f;
    --white: #ffffff;
    --ink: #000000;
    --green: #72bf14;
    --red: #c8202a;
  }
  * { margin: 0; padding: 0; box-sizing: border-box; }
  html, body {
    width: 1200px; height: 516px; overflow: hidden;
    background: var(--bg);
    font-family: "Montserrat", sans-serif;
  }
  .billboard {
    position: absolute; left: 30px; top: 68px;
    width: 1140px; height: 380px;
    background: var(--white);
    box-shadow: 4px 6px 10px rgba(0,0,0,0.45);
    overflow: hidden;
  }
  .brand {
    position: absolute; left: 40px; top: 44px;
    display: flex; align-items: center; gap: 16px;
  }
  .brand-mark { width: 58px; height: 58px; background: var(--green); }
  .brand-name {
    font-weight: 900; font-size: 62px; line-height: 0.95;
    color: var(--ink); letter-spacing: -1px;
  }
  .headline {
    position: absolute; left: 446px; top: 36px;
    font-weight: 900; font-size: 84px; line-height: 0.96;
    color: var(--ink); letter-spacing: -1px;
  }
  .visit {
    position: absolute; left: 990px; top: 60px; width: 124px;
    text-align: center; font-weight: 800; font-size: 19px; line-height: 1.2;
    color: var(--ink);
  }
  .band-services {
    position: absolute; left: 0; top: 221px; width: 100%; height: 75px;
    background: var(--green);
    display: flex; align-items: center; padding-left: 36px;
    font-weight: 800; font-size: 38px; color: var(--ink); letter-spacing: 0.5px;
  }
  .band-services .dot { margin: 0 16px; }
  .band-contact {
    position: absolute; left: 0; top: 296px; width: 100%; height: 84px;
    background: var(--ink); color: var(--white);
    display: flex; align-items: center; padding-left: 36px;
  }
  .contact-item { display: flex; align-items: center; gap: 14px; }
  .phone { font-size: 39px; font-weight: 400; }
  .phone strong { font-weight: 800; }
  .address { position: absolute; left: 562px; font-size: 27px; font-weight: 400; }
  .arrow { position: absolute; left: 990px; top: 118px; }
</style>
</head>
<body>
  <div class="billboard">
    <div class="brand">
      <span class="brand-mark"></span>
      <span class="brand-name">Summit<br>Tile</span>
    </div>

    <h1 class="headline">WE KNOW<br>FLOORING!</h1>

    <div class="visit">VISIT<br>OUR STORE</div>

    <div class="band-services">
      SUMMIT TILE<span class="dot">•</span>CABINETS<span class="dot">•</span>COUNTERTOPS
    </div>

    <div class="band-contact">
      <div class="contact-item phone">
        <svg width="38" height="38" viewBox="0 0 38 38" aria-hidden="true">
          <circle cx="19" cy="19" r="19" fill="var(--green)"/>
          <path d="M13 9c1-1 2-1 3 0l3 4c.6 1 .4 2-.4 2.6l-1.6 1.2c1 2.4 2.8 4.2 5.2 5.2l1.2-1.6c.6-.8 1.6-1 2.6-.4l4 3c1 1 1 2 0 3l-2 2c-1.6 1.6-5 .8-9-3.2S9.4 14.6 11 13z" fill="var(--ink)"/>
        </svg>
        <span>Call <strong>555-8-TILEUP</strong></span>
      </div>
      <div class="contact-item address">
        <svg width="30" height="34" viewBox="0 0 30 34" aria-hidden="true">
          <circle cx="15" cy="17" r="15" fill="var(--green)"/>
          <path d="M15 6a7 7 0 0 0-7 7c0 5 7 13 7 13s7-8 7-13a7 7 0 0 0-7-7z" fill="var(--ink)"/>
          <circle cx="15" cy="13" r="2.6" fill="var(--green)"/>
        </svg>
        <span>417 W. Hwy 82, Maple Ridge, OK 75284</span>
      </div>
    </div>

    <svg class="arrow" width="124" height="186" viewBox="0 0 124 186" aria-hidden="true">
      <path d="M46 6h34v76h38c4 0 6 3 4 7l-52 89c-4 6-10 6-14 0L4 89c-2-4 0-7 4-7h38z" fill="var(--white)"/>
      <path d="M49 6h28v78h34c3 0 4 2 3 5l-46 80c-2 4-6 4-8 0L12 89c-1-3 0-5 3-5h34z" fill="var(--red)"/>
    </svg>
  </div>
</body>
</html>
```